Carton Design

We have shipping cartons that we need to design as an advertisement. Please see attached photo

The carton is to promote our website - www.tressmarket.com.au

Attached are tress market logos

Attached is the photo of the box and the text I'd like on each side of the carton. Dimensions of the box are in the photos.

Please make the box the same colours as the tress market website (FULL COLOUR - the material will be able to take the full colour print).

```html
<!DOCTYPE html>
<html lang="en">
<head>
<meta charset="utf-8">
<title>Tress Market Shipping Carton – Panel Layout</title>
<link rel="stylesheet" href="https://fonts.googleapis.com/css2?family=Arimo:ital,wght@0,700;1,700&family=Open+Sans:wght@700;800&display=swap">
<style>
  :root {
    --backdrop: #8c8c8c;
    --panel: #ffffff;
    --green-light: #9fd43f;
    --green: #5cbf32;
    --green-dark: #2f9a35;
    --purple: #4a2468;
    --violet: #6a3296;
    --magenta: #b0237a;
    --yellow: #f6d21a;
    --logo-grey: #8f8f8f;
    --seam: #6d6d6d;
    --label: #ffffff;
  }
  * { box-sizing: border-box; margin: 0; padding: 0; }
  html, body { width: 960px; height: 1200px; overflow: hidden; background: var(--backdrop); }
  .carton-sheet { position: relative; width: 960px; height: 1200px; }

  .panel-label {
    position: absolute;
    font: 700 12px/1 "Arimo", sans-serif;
    color: var(--label);
    text-transform: uppercase;
    letter-spacing: .2px;
  }
  .panel {
    position: absolute;
    background: var(--panel);
    overflow: hidden;
    box-shadow: 0 3px 6px rgba(0,0,0,.35);
  }
  .panel svg.art { position: absolute; inset: 0; width: 100%; height: 100%; }
  .panel > * { position: absolute; }

  .wordmark {
    font: 700 24px/1 "Arimo", sans-serif;
    color: #ffffff;
    letter-spacing: -.6px;
    white-space: nowrap;
  }
  .wordmark--small { font-size: 17px; letter-spacing: -.4px; }

  .headline-yellow {
    font: 800 15px/1.25 "Open Sans", sans-serif;
    color: var(--yellow);
    text-align: right;
    transform: rotate(-4deg);
    text-shadow: 0 1px 1px rgba(0,0,0,.35);
  }
  .join-call {
    font: 800 17px/1.05 "Open Sans", sans-serif;
    color: var(--violet);
    text-align: right;
    text-transform: uppercase;
    white-space: nowrap;
  }
  .join-call--magenta { color: var(--magenta); text-align: center; font-size: 14px; }

  .logo-slot {
    font: 700 11px/1 "Arimo", sans-serif;
    color: var(--logo-grey);
    white-space: nowrap;
    text-align: center;
  }
  .logo-slot--italic { font-style: italic; font-size: 12px; }
  .logo-slot--stack { font-size: 12px; line-height: 1.05; }
  .logo-slot--tiny { font-size: 8px; line-height: 1.05; }

  .seam { height: 1px; background: var(--seam); left: 0; right: 0; }

  .dims, .care {
    font: 800 10px/1.3 "Open Sans", sans-serif;
    color: var(--purple);
    text-align: center;
    text-transform: uppercase;
  }
  .top-headline {
    font: 800 16px/1.05 "Open Sans", sans-serif;
    color: var(--violet);
    text-align: center;
    transform: rotate(-3deg);
  }
  .top-tagline {
    font: 800 13px/1 "Open Sans", sans-serif;
    color: var(--magenta);
    letter-spacing: .5px;
    transform: rotate(-3deg);
  }
  .top-join {
    font: 800 12px/1.05 "Open Sans", sans-serif;
    color: var(--yellow);
    text-align: center;
    text-shadow: 0 1px 1px rgba(0,0,0,.35);
  }
</style>
</head>
<body>
<main class="carton-sheet">

  <svg width="0" height="0" style="position:absolute">
    <defs>
      <linearGradient id="swoosh-green" x1="0" y1="0" x2="1" y2="1">
        <stop offset="0" stop-color="#a6d846"/>
        <stop offset=".55" stop-color="#5cbf32"/>
        <stop offset="1" stop-color="#2f9a35"/>
      </linearGradient>
    </defs>
  </svg>

  <!-- Front -->
  <p class="panel-label" style="left:20px;top:315px">Front of box</p>
  <section class="panel panel--front" style="left:20px;top:337px;width:320px;height:260px">
    <svg class="art" viewBox="0 0 320 260" preserveAspectRatio="none" aria-hidden="true">
      <path d="M0 8 C110 -4 230 0 320 4 V62 C250 110 130 128 0 122 Z" fill="url(#swoosh-green)"/>
      <path d="M272 0 H320 V24 Z" fill="var(--purple)"/>
    </svg>
    <p class="wordmark" style="left:14px;top:28px">www.tressmarket.com.au</p>
    <p class="headline-yellow" style="right:18px;top:66px">OVER 4,000 PRODUCTS<br>OVER 150 BRANDS!</p>
    <p class="logo-slot logo-slot--italic" style="left:6px;top:128px">PRODUCT LOGOS</p>
    <p class="logo-slot logo-slot--stack" style="left:214px;top:128px">PRODUCT<br>LOGOS</p>
    <p class="logo-slot logo-slot--italic" style="left:6px;top:146px">PRODUCT LOGOS</p>
    <p class="logo-slot logo-slot--stack" style="left:130px;top:144px">PRODUCT<br>LOGOS</p>
    <p class="logo-slot logo-slot--stack" style="left:8px;top:166px">PRODUCT<br>LOGOS</p>
    <p class="logo-slot logo-slot--tiny" style="left:74px;top:170px">PRODUCT<br>LOGOS</p>
    <p class="logo-slot logo-slot--italic" style="left:6px;top:196px">PRODUCT LOGOS</p>
    <p class="logo-slot logo-slot--stack" style="left:130px;top:190px">PRODUCT<br>LOGOS</p>
    <p class="logo-slot logo-slot--stack" style="left:8px;top:214px">PRODUCT<br>LOGOS</p>
    <p class="logo-slot" style="left:72px;top:216px">PRODUCT</p>
    <p class="logo-slot logo-slot--stack" style="left:128px;top:224px">PRODUCT<br>LOGOS</p>
    <p class="logo-slot logo-slot--italic" style="left:6px;top:243px">PRODUCT LOGOS</p>
    <p class="logo-slot logo-slot--italic" style="left:206px;top:243px">PRODUCT LOGOS</p>
    <p class="join-call" style="right:10px;top:176px">Join<br>Tressmarket<br>Today!</p>
  </section>

  <!-- Right side -->
  <p class="panel-label" style="left:415px;top:315px">Right side of box</p>
  <section class="panel panel--right" style="left:362px;top:337px;width:235px;height:260px">
    <svg class="art" viewBox="0 0 235 260" preserveAspectRatio="none" aria-hidden="true">
      <rect width="235" height="100" fill="var(--purple)"/>
      <path d="M0 6 C80 0 170 10 235 30 V62 C170 100 80 110 0 106 Z" fill="url(#swoosh-green)"/>
      <path d="M150 72 C180 60 205 62 220 78 C200 76 180 82 160 95 Z" fill="#c4e77a"/>
    </svg>
    <p class="wordmark wordmark--small" style="left:12px;top:36px">www.tressmarket.com.au</p>
    <p class="logo-slot logo-slot--stack" style="left:4px;top:112px">PRODUCT<br>LOGOS</p>
    <p class="logo-slot logo-slot--stack" style="left:90px;top:110px">PRODUCT<br>LOGOS</p>
    <p class="logo-slot logo-slot--stack" style="left:176px;top:112px">PRODUCT<br>LOGOS</p>
    <p class="logo-slot logo-slot--italic" style="left:4px;top:146px">PRODUCT LOGOS</p>
    <p class="logo-slot logo-slot--stack" style="left:176px;top:144px">PRODUCT<br>LOGOS</p>
    <p class="logo-slot logo-slot--stack" style="left:4px;top:170px">PRODUCT<br>LOGOS</p>
    <p class="logo-slot logo-slot--stack" style="left:176px;top:184px">PRODUCT<br>LOGOS</p>
    <p class="logo-slot logo-slot--stack" style="left:4px;top:204px">PRODUCT<br>LOGOS</p>
    <p class="logo-slot logo-slot--stack" style="left:176px;top:222px">PRODUCT<br>LOGOS</p>
    <p class="logo-slot logo-slot--italic" style="left:4px;top:240px">PRODUCT LOGOS</p>
    <p class="join-call join-call--magenta" style="left:62px;width:112px;top:170px">JOIN<br>TRESSMARKET<br>TODAY!</p>
  </section>

  <!-- Back -->
  <p class="panel-label" style="left:695px;top:315px">Back / reverse side of box</p>
  <section class="panel panel--back" style="left:619px;top:337px;width:320px;height:260px">
    <svg class="art" viewBox="0 0 320 260" preserveAspectRatio="none" aria-hidden="true">
      <path d="M0 8 C110 -4 230 0 320 4 V62 C250 110 130 128 0 122 Z" fill="url(#swoosh-green)"/>
      <path d="M272 0 H320 V24 Z" fill="var(--purple)"/>
    </svg>
    <p class="wordmark" style="left:14px;top:28px">www.tressmarket.com.au</p>
    <p class="headline-yellow" style="right:18px;top:66px">OVER 4,000 PRODUCTS<br>OVER 150 BRANDS!</p>
    <p class="logo-slot logo-slot--italic" style="left:6px;top:128px">PRODUCT LOGOS</p>
    <p class="logo-slot logo-slot--stack" style="left:214px;top:128px">PRODUCT<br>LOGOS</p>
    <p class="logo-slot logo-slot--italic" style="left:6px;top:146px">PRODUCT LOGOS</p>
    <p class="logo-slot logo-slot--stack" style="left:130px;top:144px">PRODUCT<br>LOGOS</p>
    <p class="logo-slot logo-slot--stack" style="left:8px;top:166px">PRODUCT<br>LOGOS</p>
    <p class="logo-slot logo-slot--tiny" style="left:74px;top:170px">PRODUCT<br>LOGOS</p>
    <p class="logo-slot logo-slot--italic" style="left:6px;top:196px">PRODUCT LOGOS</p>
    <p class="logo-slot logo-slot--stack" style="left:130px;top:190px">PRODUCT<br>LOGOS</p>
    <p class="logo-slot logo-slot--stack" style="left:8px;top:214px">PRODUCT<br>LOGOS</p>
    <p class="logo-slot" style="left:72px;top:216px">PRODUCT</p>
    <p class="logo-slot logo-slot--stack" style="left:128px;top:224px">PRODUCT<br>LOGOS</p>
    <p class="logo-slot logo-slot--italic" style="left:6px;top:243px">PRODUCT LOGOS</p>
    <p class="logo-slot logo-slot--italic" style="left:206px;top:243px">PRODUCT LOGOS</p>
    <p class="join-call" style="right:10px;top:176px">Join<br>Tressmarket<br>Today!</p>
  </section>

  <!-- Bottom -->
  <p class="panel-label" style="left:20px;top:627px">Bottom of box (with top and bottom flaps)</p>
  <section class="panel panel--bottom" style="left:20px;top:649px;width:320px;height:236px">
    <svg class="art" viewBox="0 0 320 236" preserveAspectRatio="none" aria-hidden="true">
      <path d="M0 48 C90 30 220 26 320 22 V112 C240 150 120 160 0 150 Z" fill="url(#swoosh-green)"/>
    </svg>
    <p class="wordmark" style="left:14px;top:68px">www.tressmarket.com.au</p>
    <div class="seam" style="top:118px"></div>
    <p class="headline-yellow" style="right:18px;top:104px">OVER 4,000 PRODUCTS<br>OVER 150 BRANDS!</p>
  </section>

  <!-- Left side -->
  <p class="panel-label" style="left:425px;top:627px">Left side of box</p>
  <section class="panel panel--left" style="left:362px;top:649px;width:235px;height:236px">
    <svg class="art" viewBox="0 0 235 236" preserveAspectRatio="none" aria-hidden="true">
      <path d="M160 0 H235 V70 C200 62 172 40 160 0 Z" fill="url(#swoosh-green)"/>
      <path d="M22 100 L44 74 L66 100 H53 V172 H35 V100 Z" fill="var(--green-dark)"/>
      <path d="M169 100 L191 74 L213 100 H200 V172 H182 V100 Z" fill="var(--green-dark)"/>
    </svg>
    <p class="dims" style="left:0;right:0;top:58px">38 X 28 X 31 CM</p>
    <p class="care" style="left:0;right:0;top:96px">Very fragile</p>
    <p class="care" style="left:0;right:0;top:124px">Handle<br>with<br>care</p>
  </section>

  <!-- Top -->
  <p class="panel-label" style="left:672px;top:627px">Top of box (with top and bottom flaps)</p>
  <section class="panel panel--top" style="left:619px;top:649px;width:320px;height:236px">
    <svg class="art" viewBox="0 0 320 236" preserveAspectRatio="none" aria-hidden="true">
      <path d="M0 0 H320 V6 C220 16 100 14 0 22 Z" fill="url(#swoosh-green)"/>
      <path d="M0 110 C100 88 230 84 300 92 C320 100 300 120 250 140 C170 168 70 176 0 172 Z" fill="url(#swoosh-green)"/>
      <path d="M0 214 C110 196 230 196 320 204 V236 H0 Z" fill="url(#swoosh-green)"/>
    </svg>
    <p class="top-headline" style="left:40px;right:40px;top:30px">OVER 4,000 PRODUCTS<br>AVAILABLE ONLINE</p>
    <p class="top-tagline" style="left:0;right:0;top:68px;text-align:center">RELIABLE • SAFE • FAST</p>
    <p class="wordmark wordmark--small" style="left:14px;top:112px">www.tressmarket.com.au</p>
    <p class="top-join" style="right:30px;top:130px">JOIN<br>TRESSMARKET<br>TODAY!</p>
  </section>

</main>
</body>
</html>
```